Baby Girl Maud Birth Announcement for Dec 1st 2020

Using an existing photo from an artist, build a 2 sided card with messaging and details on opposite side.

Style: fun, timeless, elegant, vibrant
Side 1:
Text "Welcome Maud".
Use file called FRONT BACKGROUND - Welcome Maud.
Consider 2 fonts, consider 2 colors of words. use provided image and monochromatic image of a heart
Side 2 content to be fit:
"Welcome to our little ray of light!"
"Maud Iris Jane Pelham"
Date of birth ---/--/----
Time of birth
Weight
Length
"Loving and Proud Parents : Clara Pelham - Ter Horst & Gregor Pelham"
Amazing and Wonderful God Parents : "Lehuanani Kekoa & Bastien De Wulf" + "Mira Chen Holloway & Dustin Holloway "

Target Market(s)

Family and friends.
International audience (european/asian/american).
Urban, up market,

Requirements
Must have
• Use file called FRONT BACKGROUND - Welcome Maud on the front
Nice to have
• Consider 2 fonts, consider 2 colors of words. use provided image and monochromatic image of a heart

```html
<!DOCTYPE html>
<html lang="en">
<head>
<meta charset="utf-8">
<title>Maud Iris Jane Pelham – Birth Announcement</title>
<link rel="stylesheet" href="https://fonts.googleapis.com/css2?family=Allura&family=Poppins:ital,wght@0,400;0,500;0,600;1,400;1,500&display=swap">
<style>
  :root {
    --page-bg: #efece6;
    --card-bg: #ffffff;
    --heart-light: #e2e2e4;
    --heart-mid: #c4c4c7;
    --heart-dark: #a9a9ad;
    --ink-sage: #7f8a86;
    --ink-slate: #6f8e99;
    --ink-grey: #8b8b8b;
  }
  * { margin: 0; padding: 0; box-sizing: border-box; }
  html, body {
    width: 1200px;
    height: 1200px;
    overflow: hidden;
    background: var(--page-bg);
  }
  .canvas {
    position: relative;
    width: 1200px;
    height: 1200px;
  }
  .card {
    position: absolute;
    left: 40px;
    top: 237px;
    width: 1120px;
    height: 726px;
    background: var(--card-bg);
    box-shadow: 0 4px 14px rgba(0, 0, 0, 0.12);
    overflow: hidden;
    text-align: center;
    font-family: "Poppins", sans-serif;
  }
  .heart-confetti {
    position: absolute;
    left: 0;
    top: 0;
    width: 100%;
    height: 300px;
    background: linear-gradient(180deg,
      var(--heart-mid) 0%,
      var(--heart-light) 45%,
      rgba(255, 255, 255, 0) 100%);
    opacity: 0.75;
  }
  .side-heart {
    position: absolute;
    top: 296px;
    width: 41px;
    height: 40px;
    border-radius: 50%;
    background: var(--heart-mid);
  }
  .side-heart--left { left: 152px; }
  .side-heart--right { left: 1052px; }
  .line {
    position: absolute;
    left: 0;
    width: 100%;
    white-space: nowrap;
  }
  .welcome {
    top: 213px;
    font-size: 27px;
    font-style: italic;
    font-weight: 500;
    color: var(--ink-sage);
  }
  .baby-name {
    top: 270px;
    font-family: "Allura", cursive;
    font-size: 80px;
    line-height: 1.2;
    color: var(--ink-slate);
  }
  .birth-details {
    top: 378px;
    font-size: 18px;
    font-weight: 600;
    letter-spacing: 0.22em;
    color: var(--ink-slate);
  }
  .birth-details .sep { margin: 0 0.9em; }
  .role-title {
    font-size: 18px;
    color: var(--ink-slate);
  }
  .role-title--parents { top: 537px; font-style: italic; font-weight: 500; }
  .role-title--godparents { top: 604px; font-size: 19px; font-weight: 500; }
  .role-names {
    font-size: 16.5px;
    font-weight: 400;
    color: var(--ink-grey);
  }
  .role-names--parents { top: 567px; }
  .role-names--godparents { top: 636px; }
</style>
</head>
<body>
<div class="canvas">
  <section class="card">
    <div class="heart-confetti" role="img" aria-label="Scattered silver-grey heart confetti falling from the top edge"></div>
    <div class="side-heart side-heart--left" role="img" aria-label="Small grey heart"></div>
    <div class="side-heart side-heart--right" role="img" aria-label="Small grey heart"></div>

    <p class="line welcome">Welcome to our little ray of light!</p>
    <h1 class="line baby-name">Maud Iris Jane Pelham</h1>
    <p class="line birth-details">
      <span>01/12/2020</span><span class="sep">|</span><span>12:00 AM</span><span class="sep">|</span><span>3500 GRAM</span><span class="sep">|</span><span>55 CM</span>
    </p>

    <p class="line role-title role-title--parents">~ Loving and Proud Parents ~</p>
    <p class="line role-names role-names--parents">Clara Pelham - Ter Horst &amp; Gregor Pelham</p>
    <p class="line role-title role-title--godparents">~ Amazing and Wonderful God Parents ~</p>
    <p class="line role-names role-names--godparents">Lehuanani Kekoa &amp; Bastien De Wulf + Mira Chen Holloway &amp; Dustin Holloway</p>
  </section>
</div>
</body>
</html>
```